New Pain Management Physcian Private Practice webpage design

Interventional Pain Management Company looking for new website. Want it modeled very closely to http://www.brivoltclinic.example/ website. Under navigation panel at top of main webpage take off the following tabs: About, Locations, News, Testimonial, and Pain Channel. Add New Patient visit tab, change about to Main Page, change treatments to Procedures, change Providers to Provider.Main web page should have the KTR logo, no picture slideshow for now but want ability to add pictures to the slideshow in the future. Pictures are included to show you an idea of what main page should look like. Colors are teal,Deep Navy, and White as shown in KTR logo. Font style should also be same as KTR logo.

Target Market(s)

Patients with all kinda of acute and chronic pain. Especially neck, mid back,low back pain, and joint pain.

Industry/Entity Type

Medical

Coding

Number of Pages Required

5+ page

Requirements
Must have
• See Project description above
Nice to have
• ability to add pictures to the slideshow in future
Should not have
• not applicable

```html
<!DOCTYPE html>
<html lang="en">
<head>
<meta charset="utf-8">
<title>Kestrel Therapeutic Relief</title>
<link href="https://fonts.googleapis.com/css2?family=Raleway:wght@300;400;600;700&family=Open+Sans:wght@400;600&display=swap" rel="stylesheet">
<style>
:root{
  --teal:#1b9bb0;
  --teal-light:#5cc3d3;
  --navy:#13303f;
  --navy-deep:#0d2431;
  --ink:#333b40;
  --muted:#7a858b;
  --line:#d9dee1;
  --paper:#ffffff;
  --mist:#eef1f2;
}
*{box-sizing:border-box;margin:0;padding:0}
html,body{width:900px;height:1200px;overflow:hidden}
body{font-family:'Open Sans',Arial,sans-serif;color:var(--ink);background:var(--mist);font-size:9px;line-height:1.5}
.page{width:900px;height:1200px;position:relative;background:var(--paper)}
.topbar{height:105px;background:radial-gradient(circle at 70% 30%,#2a5766 0,var(--navy) 45%,var(--navy-deep) 100%);position:relative}
.brand{position:absolute;left:40px;top:20px;display:flex;align-items:center;gap:10px;font-family:'Raleway',sans-serif;color:#fff}
.brand-mark{width:44px;height:44px;background:var(--teal);border-radius:4px}
.brand-name{font-weight:700;font-size:16px;letter-spacing:2px}
.brand-sub{font-size:8px;letter-spacing:1px;color:#cfe6ea;font-weight:400}
.top-actions{position:absolute;left:330px;top:14px;display:flex;gap:6px}
.top-actions a{background:var(--teal);color:#fff;font-family:'Raleway',sans-serif;font-size:8px;font-weight:600;padding:6px 12px;text-decoration:none;border-radius:2px;letter-spacing:.5px}
.phone{position:absolute;right:40px;top:16px;color:#fff;font-family:'Raleway',sans-serif;font-size:13px;font-weight:600}
.nav{position:absolute;left:40px;right:40px;top:108px;height:22px;background:#fff;display:flex;justify-content:space-between;align-items:center;padding:0 18px;border-bottom:1px solid var(--line)}
.nav a{font-family:'Raleway',sans-serif;font-size:8px;font-weight:700;color:var(--muted);text-decoration:none;letter-spacing:.8px}
.nav a.current{color:var(--navy)}
.hero{position:absolute;left:40px;right:40px;top:136px;height:200px;background:linear-gradient(180deg,#f7f9fa,#e8edef);display:flex}
.hero-photo{width:480px;height:200px;background:linear-gradient(135deg,#dfe5e8,#b9c4c9)}
.hero-copy{padding:40px 30px 0 30px;flex:1}
.eyebrow{font-family:'Raleway',sans-serif;color:var(--teal);font-size:11px;letter-spacing:1px;font-weight:600}
.hero h1{font-family:'Raleway',sans-serif;color:var(--teal);font-size:34px;font-weight:700;line-height:1.1;margin:4px 0 10px}
.hero p{color:var(--muted);font-size:8px;margin-bottom:12px}
.btn-outline{display:inline-block;border:1px solid var(--teal);color:var(--teal);font-family:'Raleway',sans-serif;font-size:8px;font-weight:700;padding:5px 10px;letter-spacing:.5px}
.columns{position:absolute;left:40px;right:40px;top:355px;display:flex;gap:30px}
.col{flex:1}
.col-head{display:flex;align-items:flex-end;gap:8px;border-bottom:2px solid var(--teal);padding-bottom:4px;margin-bottom:12px}
.col-head small{font-family:'Raleway',sans-serif;color:var(--muted);font-size:9px;line-height:1.1}
.col-head h2{font-family:'Raleway',sans-serif;color:var(--teal);font-size:30px;font-weight:700;line-height:1}
.lead{font-weight:600;color:var(--ink);margin-bottom:6px}
.body-copy{color:var(--muted);margin-bottom:8px}
.read-more{color:var(--teal);font-weight:600}
.hours{margin-top:24px}
.hours h3{font-family:'Raleway',sans-serif;font-size:14px;color:var(--navy);margin-bottom:6px}
.quick{list-style:none;margin-top:24px}
.quick li{font-family:'Raleway',sans-serif;font-weight:700;font-size:8px;color:var(--navy);padding:3px 0;display:flex;align-items:center;gap:6px}
.quick li svg{flex:none}
.news-list{list-style:none}
.news-list li{display:flex;gap:6px;margin-bottom:10px;color:var(--ink)}
.news-list li span{color:var(--teal);font-weight:700}
.see-all{font-family:'Raleway',sans-serif;color:var(--teal);font-weight:700;font-size:10px;letter-spacing:1px}
.doctor-photo{width:100%;height:330px;background:linear-gradient(180deg,#e6eaec,#9aa6ac)}
.doctor-name{font-family:'Raleway',sans-serif;font-weight:700;color:var(--navy);font-size:11px;margin-top:8px}
.doctor-title{color:var(--muted)}
.footer{position:absolute;left:0;right:0;top:840px;height:330px;background:var(--navy);color:#b9c8cf;padding:30px 40px;display:flex;gap:30px}
.footer h4{font-family:'Raleway',sans-serif;color:var(--teal-light);font-size:9px;letter-spacing:1px;margin-bottom:10px}
.f-treat{width:260px}
.f-treat ul{list-style:none;columns:2}
.f-treat li{font-size:8px;padding:1px 0}
.social{display:flex;gap:8px;margin-top:14px}
.social span{width:16px;height:16px;border-radius:50%;background:var(--teal)}
.f-links{width:230px;display:grid;grid-template-columns:1fr 1fr;row-gap:14px;align-content:start;padding-top:20px}
.f-links a{color:#b9c8cf;font-family:'Raleway',sans-serif;font-size:8px;font-weight:700;text-decoration:none;letter-spacing:1px}
.f-contact{flex:1}
.f-contact p{font-size:8px;margin-bottom:8px}
.map{height:150px;background:linear-gradient(135deg,#1f4656,#173746)}
.legal{position:absolute;left:0;right:0;top:1170px;height:30px;background:var(--navy-deep);color:#7f949c;font-size:7px;display:flex;justify-content:space-between;align-items:center;padding:0 40px}
.legal nav{display:flex;gap:14px}
</style>
</head>
<body>
<div class="page">
  <header class="topbar">
    <div class="brand">
      <span class="brand-mark"></span>
      <div><div class="brand-name">KESTREL</div><div class="brand-sub">THERAPEUTIC RELIEF</div></div>
    </div>
    <div class="top-actions">
      <a href="#">REQUEST AN APPOINTMENT</a>
      <a href="#">PT PORTAL</a>
      <a href="#">WATCH TREATMENT VIDEOS</a>
    </div>
    <div class="phone">(555) 014-2290</div>
  </header>

  <nav class="nav">
    <a class="current" href="#">HOME</a><a href="#">NEW PATIENT VISIT</a><a href="#">PROVIDER</a><a href="#">PROCEDURES</a><a href="#">INSURANCE</a><a href="#">FAQ</a><a href="#">FORMS</a><a href="#">CONTACT</a>
  </nav>

  <section class="hero">
    <div class="hero-photo" role="img" aria-label="Slideshow photo: relaxed woman leaning back in an office chair"></div>
    <div class="hero-copy">
      <div class="eyebrow">KESTREL THERAPEUTIC RELIEF</div>
      <h1>FEEL<br>RELIEVED</h1>
      <p>KTR is a comprehensive, full time pain management practice. Using a variety of methods, our specialist finds the source of your pain and recommends the best, most effective way to treat it.</p>
      <span class="btn-outline">REQUEST AN APPOINTMENT</span>
    </div>
  </section>

  <section class="columns">
    <div class="col">
      <div class="col-head"><small>About</small><h2>KTR</h2></div>
      <p class="lead">Manage your pain and get back into life.</p>
      <p class="body-copy">KTR is a comprehensive, full time pain management practice. Our trained specialist uses a variety of methods to find the source of your pain and recommends the treatment most effective for you.</p>
      <p class="read-more">Read More</p>
      <div class="hours">
        <h3>OFFICE HOURS:</h3>
        <p>M-F 8:00 am – 5:00 pm</p>
        <p>Office closed from 12:00 pm – 1:00 pm</p>
      </div>
      <ul class="quick">
        <li><svg width="8" height="8" viewBox="0 0 8 8"><path d="M2 1l4 3-4 3" fill="none" stroke="#1b9bb0" stroke-width="1.5"/></svg>MEET THE PROVIDER</li>
        <li><svg width="8" height="8" viewBox="0 0 8 8"><path d="M2 1l4 3-4 3" fill="none" stroke="#1b9bb0" stroke-width="1.5"/></svg>PATIENT FORMS</li>
        <li><svg width="8" height="8" viewBox="0 0 8 8"><path d="M2 1l4 3-4 3" fill="none" stroke="#1b9bb0" stroke-width="1.5"/></svg>FAQ</li>
        <li><svg width="8" height="8" viewBox="0 0 8 8"><path d="M2 1l4 3-4 3" fill="none" stroke="#1b9bb0" stroke-width="1.5"/></svg>ACCEPTED INSURANCE</li>
        <li><svg width="8" height="8" viewBox="0 0 8 8"><path d="M2 1l4 3-4 3" fill="none" stroke="#1b9bb0" stroke-width="1.5"/></svg>REQUEST APPOINTMENT</li>
      </ul>
    </div>

    <div class="col">
      <div class="col-head"><small>Latest</small><h2>NEWS</h2></div>
      <ul class="news-list">
        <li><span>›</span>Manage your pain and get back into life. Manage your pain and get back into life.</li>
        <li><span>›</span>Manage your pain and get back into life.</li>
        <li><span>›</span>Manage your pain and get back into life. Manage your pain and get back into life.</li>
        <li><span>›</span>Manage your pain and get back into life.</li>
        <li><span>›</span>Manage your pain and get back into life. Manage your pain and get back into life.</li>
        <li><span>›</span>Manage your pain and get back into life.</li>
        <li><span>›</span>Manage your pain and get back into life. Manage your pain and get back into life.</li>
        <li><span>›</span>Manage your pain and get back into life. Manage your pain and get back into life.</li>
      </ul>
      <p class="see-all">SEE ALL ››</p>
    </div>

    <div class="col">
      <div class="col-head"><small>Your</small><h2>DOCTOR</h2></div>
      <div class="doctor-photo" role="img" aria-label="Portrait photo of the practice physician in a suit"></div>
      <p class="doctor-name">DANIEL REYES MD</p>
      <p class="doctor-title">Double Board Certified in PM&amp;R and Interventional Pain Management</p>
    </div>
  </section>

  <footer class="footer">
    <div class="f-treat">
      <h4>THE LEADING MEDICAL TREATMENTS FOR PAIN</h4>
      <ul>
        <li>Back Pain</li><li>Neck Pain</li><li>Joint Pain</li><li>Knee Pain</li><li>Hip Pain</li><li>Sciatica</li><li>Shoulder Pain</li><li>Headaches</li><li>Nerve Pain</li><li>Arthritis</li><li>Spine Injury</li><li>Sports Injuries</li>
      </ul>
      <div class="social"><span></span><span></span><span></span></div>
    </div>
    <div class="f-links">
      <a href="#">HOME</a><a href="#">INSURANCE</a>
      <a href="#">NEW PATIENT VISIT</a><a href="#">FAQ</a>
      <a href="#">PROVIDER</a><a href="#">FORMS</a>
      <a href="#">PROCEDURES</a><a href="#">CONTACT</a>
    </div>
    <div class="f-contact">
      <h4>KESTREL THERAPEUTIC RELIEF</h4>
      <p>210 Harbor Lane, Suite 5, Fairview, ST 00412<br>Tel: (555) 014-2290<br>info@brivoltclinic.example</p>
      <div class="map" role="img" aria-label="Street map showing the clinic location"></div>
    </div>
  </footer>

  <div class="legal">
    <span>COPYRIGHT © KTR. ALL RIGHTS RESERVED</span>
    <nav><span>CAREERS</span><span>TERMS &amp; CONDITIONS</span><span>PRIVACY POLICY</span><span>SITE MAP</span></nav>
  </div>
</div>
</body>
</html>
```